HVAC Door Hanger- 4.25 inches by 11 inches

Hello We are using the Brightvale door hanger as an inspiration for our new door hanger. The company name is Corvant Home Services. Logo files attached. The Slogan needs to be added on the front with the Logo "Southern California’s Trusted Name in Home Services". Instead of the X protection plan, the name will be Full Shield by Corvant or Corvant Climate Keeper- The slogan for this package will be "Peace of Mind, For Every Season

```html
<!DOCTYPE html>
<html lang="en">
<head>
<meta charset="utf-8">
<title>Corvant Home Services – Door Hanger</title>
<link href="https://fonts.googleapis.com/css2?family=Montserrat:wght@600;700;800&family=Oswald:wght@700&display=swap" rel="stylesheet">
<style>
  :root {
    --blue: #1a75b0;
    --blue-deep: #0f4d7a;
    --orange: #f5a020;
    --white: #ffffff;
    --hole: #231f20;
    --page: #ffffff;
  }
  * { box-sizing: border-box; margin: 0; padding: 0; }
  html, body { width: 1200px; height: 1200px; overflow: hidden; background: var(--page); }
  body { position: relative; font-family: 'Montserrat', sans-serif; }

  .hanger {
    position: absolute;
    top: 498px;
    width: 528px;
    height: 204px;
    box-shadow: 0 6px 8px rgba(0,0,0,0.28);
    overflow: hidden;
  }
  .hole {
    position: absolute;
    width: 58px; height: 58px;
    border-radius: 50%;
    background: var(--hole);
  }

  /* Front */
  .hanger--front { left: 41px; background: var(--blue); }
  .front-inner {
    position: absolute; inset: 6px;
    background: var(--white);
  }
  .front-frame {
    position: absolute; inset: 8px;
    border: 5px solid var(--orange);
    border-radius: 10px;
  }
  .front-brand {
    position: absolute;
    left: 48px; top: 62px;
    display: flex; align-items: center; gap: 12px;
    font-weight: 800; font-size: 34px; line-height: 1;
    color: var(--blue);
    letter-spacing: 0.5px;
  }
  .front-brand .mark {
    width: 22px; height: 22px; border-radius: 50%;
    background: var(--orange);
  }
  .front-brand .name { white-space: nowrap; }
  .front-brand .name small { display: block; font-size: 34px; }
  .front-slogan {
    position: absolute;
    left: 22px; right: 22px; top: 159px; height: 23px;
    background: var(--blue);
    border-radius: 4px;
    color: var(--white);
    font-weight: 700; font-size: 12.5px;
    display: flex; align-items: center; justify-content: center;
  }
  .hanger--front .hole { left: 439px; top: 74px; }

  /* Back */
  .hanger--back { left: 638px; background: var(--white); }
  .back-plan {
    position: absolute; left: 0; top: 0; bottom: 0; width: 219px;
    background: var(--blue);
  }
  .back-plan__lower {
    position: absolute; left: 0; right: 0; top: 136px; bottom: 0;
    background: var(--blue-deep);
    color: var(--white);
    font-weight: 700; font-size: 15.5px; line-height: 1.3;
    display: flex; align-items: center; justify-content: center; text-align: center;
  }
  .back-tab {
    position: absolute; left: 32px; top: 0; width: 156px; height: 58px;
    background: var(--white);
    border-radius: 0 0 8px 8px;
    display: flex; align-items: center; justify-content: center;
    color: var(--blue); font-weight: 800; font-size: 13px; text-align: center; line-height: 1.15;
  }
  .back-title {
    position: absolute; left: 0; right: 0; top: 70px;
    font-family: 'Oswald', sans-serif; font-weight: 700;
    font-size: 23px; line-height: 1.15;
    color: var(--white); text-align: center;
    text-transform: uppercase;
  }
  .back-phone {
    position: absolute; left: 219px; right: 0; top: 14px;
    text-align: center;
    color: var(--orange); font-weight: 800; font-size: 30px;
  }
  .back-services {
    position: absolute; left: 225px; top: 64px; width: 297px; height: 134px;
    background: var(--orange);
    list-style: none;
    padding: 9px 0 0 16px;
    color: var(--white); font-weight: 800; font-size: 21px; line-height: 29px;
  }
  .back-services li::before { content: "•"; margin-right: 5px; font-size: 16px; vertical-align: 3px; }
  .hanger--back .hole { left: 440px; top: 74px; }
</style>
</head>
<body>
  <section class="hanger hanger--front" aria-label="Door hanger front">
    <div class="front-inner">
      <div class="front-frame"></div>
    </div>
    <div class="front-brand">
      <span class="mark"></span>
      <span class="name">CORVANT<small>HOME SERVICES</small></span>
    </div>
    <div class="front-slogan">SOUTHERN CALIFORNIA’S TRUSTED NAME IN HOME SERVICES</div>
    <span class="hole"></span>
  </section>

  <section class="hanger hanger--back" aria-label="Door hanger back">
    <div class="back-plan">
      <div class="back-tab">CORVANT<br>HOME SERVICES</div>
      <h2 class="back-title">Full Shield<br>by Corvant</h2>
      <p class="back-plan__lower">PEACE OF MIND,<br>FOR EVERY SEASON</p>
    </div>
    <p class="back-phone">(555) 214-7390</p>
    <ul class="back-services">
      <li>HEATING</li>
      <li>COOLING</li>
      <li>PLUMBING</li>
      <li>ELECTRICAL</li>
    </ul>
    <span class="hole"></span>
  </section>
</body>
</html>
```